MODELS AGENCY NEW YEAR 2026 CARD

A 10 cm x 21 cm horizontal New Year card for clients of our 2 models agencies, Pommelin (kids) and Velvaride (actors and adults) (logo in the jobs).

Side A of the card: creative mission:
-text: 2026
-text: Peace and Love
-Studio or movie set atmosphere
-tone of voice: optimistic, positive, colorful

Side B:
(name of 4 people of the agency:)
Odette, Anne-Sophie, Hortense & Luc-Antoine,
(2 logos)
Pommelin & VelvaRide
(Adres)
Rue des Tilleuls 74 b3 - 1200 Bruxelles - Belgique

Target Market(s)

Movie directors, photographers

Industry/Entity Type

Fashion, advertising & Movies

Requirements
Must have
• SEE TEXT IN BRIEFING

```html
<!DOCTYPE html>
<html lang="fr">
<head>
<meta charset="utf-8">
<title>Pommelin &amp; VelvaRide — Carte de vœux 2026</title>
<link rel="stylesheet" href="https://fonts.googleapis.com/css2?family=Ubuntu:wght@400;500;700&family=Barlow+Condensed:wght@500&display=swap">
<style>
  :root {
    --page-bg: #e4e4e4;
    --card-white: #ffffff;
    --ink-purple: #3b1f5e;
    --accent-blue: #29a3df;
    --night-black: #090d0e;
    --deep-teal: #104a50;
    --silver-light: #d9d9d9;
    --silver-mid: #a9a9a9;
    --numeral-white: #ffffff;
    --numeral-shade: #b5b5b5;
    --tag-white: #ffffff;
    --tag-ink: #e2582a;
  }
  * { margin: 0; padding: 0; box-sizing: border-box; }
  html, body {
    width: 1200px; height: 1200px; overflow: hidden;
    background: var(--page-bg);
  }
  .card {
    position: absolute; left: 50px; top: 338px;
    width: 1100px; height: 524px;
    display: flex;
    font-family: "Ubuntu", sans-serif;
  }
  .card-back {
    position: relative; width: 550px; height: 100%;
    background: var(--card-white);
    color: var(--ink-purple);
    text-align: center;
  }
  .brand-name {
    position: absolute; left: 0; right: 0; top: 112px;
    display: flex; align-items: center; justify-content: center; gap: 14px;
    font-size: 46px; font-weight: 500; letter-spacing: 1px;
    color: var(--ink-purple);
  }
  .brand-square {
    width: 22px; height: 22px; background: var(--accent-blue);
  }
  .team-names {
    position: absolute; left: 0; right: 0; top: 296px;
    font-size: 18px; line-height: 22px;
  }
  .agencies {
    position: absolute; left: 0; right: 0; top: 376px;
    font-size: 18px;
  }
  .address {
    position: absolute; left: 0; right: 0; top: 428px;
    font-size: 18px;
  }
  .card-front {
    position: relative; width: 550px; height: 100%;
    background: linear-gradient(90deg, var(--night-black) 0%, #132427 35%, var(--deep-teal) 100%);
    overflow: hidden;
  }
  .year {
    position: absolute; left: 92px; top: 40px;
    font-family: "Barlow Condensed", sans-serif;
    font-weight: 500;
    font-size: 268px; line-height: 190px;
    letter-spacing: -6px;
    background: linear-gradient(90deg, var(--numeral-white) 0%, var(--numeral-white) 55%, var(--numeral-shade) 100%);
    -webkit-background-clip: text; background-clip: text;
    color: transparent;
  }
  .year span { display: block; }
  .slogan-tag {
    position: absolute; left: 383px; top: 0;
    width: 125px; height: 213px;
    background: linear-gradient(90deg, var(--silver-mid) 0%, var(--silver-light) 45%, var(--silver-mid) 100%);
    padding: 58px 10px 0 0;
    text-align: right;
    font-size: 31px; line-height: 42px;
    color: #111;
  }
  .partner-tag {
    position: absolute; left: 383px; top: 377px;
    width: 125px; height: 97px;
    background: var(--tag-white);
    display: flex; align-items: center; justify-content: center;
    font-size: 22px; font-weight: 500;
    color: var(--tag-ink);
  }
</style>
</head>
<body>
  <main class="card">
    <section class="card-back">
      <div class="brand-name"><span class="brand-square"></span>Pommelin</div>
      <p class="team-names">Odette, Anne-Sophie,<br>Hortense &amp; Luc-Antoine</p>
      <p class="agencies">Pommelin &amp; VelvaRide</p>
      <p class="address">Rue des Tilleuls 74 b3 - 1200 Bruxelles - Belgique</p>
    </section>
    <section class="card-front">
      <h1 class="year"><span>20</span><span>26</span></h1>
      <div class="slogan-tag">Peace<br>and<br>Love</div>
      <div class="partner-tag">VelvaRide</div>
    </section>
  </main>
</body>
</html>
```